Ridgeline Elite

Letter Head, Envelope, Business Cards, Social Media Banner (FB/Twitter), Social Media Icon, Social Media Announcement Template...

We are a Softball Team/Organization

Target Market(s)

High School Student-Athletes (softball players) and their parents

Font styles to use
Serif

Requirements
Must have
• Logo & Colors
Must POP and say WOW
Common theme amongst all designs

```html
<!DOCTYPE html>
<html lang="en">
<head>
<meta charset="utf-8">
<title>Ridgeline Elite – Stationery</title>
<link href="https://fonts.googleapis.com/css2?family=Tinos:wght@400;700&family=Lato:wght@300;400;700&family=Pinyon+Script&display=swap" rel="stylesheet">
<style>
  :root{
    --navy:#1c3461;
    --navy-deep:#1a2f58;
    --navy-light:#2d5192;
    --band-grey:#b8bfcc;
    --paper:#f0eff0;
    --backdrop:#dcdcdc;
    --ink:#3a3a3a;
    --ink-dark:#111;
  }
  *{box-sizing:border-box;margin:0;padding:0}
  html,body{width:1200px;height:945px;overflow:hidden;background:var(--backdrop)}
  .canvas{position:relative;width:1200px;height:945px}
  .sheet{position:absolute;background:var(--paper);box-shadow:0 2px 8px rgba(0,0,0,.12);overflow:hidden}
  .wordmark{position:absolute;font-family:'Tinos',serif;font-weight:700;color:var(--navy);white-space:nowrap;letter-spacing:.5px}
  .contact{position:absolute;font-family:'Tinos',serif;color:var(--ink-dark);white-space:nowrap}
  .contact li{list-style:none;display:flex;align-items:center}
  .contact svg{fill:var(--navy);flex:none}
  .band{position:absolute;left:0;right:0;background:var(--band-grey)}
  .band-navy{position:absolute;left:0;top:0;bottom:0;background:var(--navy);color:#fff;font-family:'Tinos',serif;display:flex;align-items:center;white-space:nowrap}

  /* Letterhead */
  .letterhead{left:126px;top:103px;width:570px;height:739px}
  .letterhead .wordmark{left:47px;top:36px;font-size:21px}
  .letterhead .divider{position:absolute;left:376px;top:39px;width:1px;height:32px;background:#999}
  .letterhead .contact{left:386px;top:39px;font-size:9px;line-height:11px}
  .letterhead .contact svg{width:7px;height:7px;margin-right:6px}
  .letter-body{position:absolute;left:83px;top:161px;width:404px;font-family:'Lato',sans-serif;font-weight:300;font-size:8.6px;line-height:12.3px;color:var(--ink)}
  .letter-body .date{margin-bottom:12px}
  .letter-body .recipient{margin-bottom:20px}
  .letter-body .recipient strong{font-weight:700;color:var(--ink-dark)}
  .letter-body .salutation{margin-bottom:12px}
  .letter-body p.para{margin-bottom:12px;text-align:justify}
  .letter-body .closing{margin-top:31px}
  .letter-body .signature{font-family:'Pinyon Script',cursive;font-size:18px;color:var(--ink-dark);margin-top:6px;margin-left:4px}
  .letterhead .band{top:713px;height:13px}
  .letterhead .band-navy{width:504px;padding-left:46px;font-size:9px}

  /* Envelope */
  .envelope{left:578px;top:265px;width:523px;height:227px}
  .envelope .wordmark{left:32px;top:25px;font-size:19px}
  .envelope .dash{position:absolute;left:31px;top:157px;width:15px;height:1.5px;background:var(--navy)}
  .envelope .contact{left:31px;top:168px;font-size:7.3px;line-height:9.3px}
  .envelope .contact svg{width:6px;height:6px;margin-right:5px}
  .envelope .band{top:206px;height:10px}
  .envelope .band-navy{width:478px;padding-left:30px;font-size:7.3px}

  /* Business cards */
  .card{width:265px;height:151px}
  .card-front-a{left:578px;top:514px}
  .card-front-b{left:719px;top:690px}
  .card-front .wordmark{left:22px;top:66px;font-size:15px}
  .card-front .divider{position:absolute;left:133px;top:43px;width:1px;height:66px;background:#999}
  .card-front .details{position:absolute;left:146px;top:44px;font-family:'Tinos',serif;color:var(--ink-dark)}
  .card-front .name{font-weight:700;font-size:7.5px;color:var(--navy);line-height:8px}
  .card-front .role,.card-front .address{font-size:5.6px;line-height:7.5px}
  .card-front .address{margin-top:6px}
  .card-front .contact{position:static;font-size:5.6px;line-height:7.5px;margin-top:6px}
  .card-front .contact svg{width:4.5px;height:4.5px;margin-right:4px}
  .card-front .band{top:135px;height:9px}
  .card-front .band-navy{width:220px}

  .card-back{left:869px;top:514px;background:linear-gradient(115deg,var(--navy-deep) 0%,var(--navy-deep) 45%,var(--navy-light) 100%)}
  .card-back .wordmark{left:28px;top:80px;font-size:17px;color:#fff}
</style>
</head>
<body>
<svg width="0" height="0" style="position:absolute" aria-hidden="true">
  <symbol id="icon-phone" viewBox="0 0 24 24"><path d="M6.6 10.8a15 15 0 0 0 6.6 6.6l2.2-2.2c.3-.3.7-.4 1-.2 1.1.4 2.3.6 3.6.6.6 0 1 .4 1 1V20c0 .6-.4 1-1 1A17 17 0 0 1 3 4c0-.6.4-1 1-1h3.5c.6 0 1 .4 1 1 0 1.3.2 2.5.6 3.6.1.3 0 .7-.2 1z"/></symbol>
  <symbol id="icon-mail" viewBox="0 0 24 24"><path d="M2 5h20v14H2z M3.5 6.5 12 13l8.5-6.5" fill="none" stroke="currentColor"/><path d="M2 5h20v14H2zM4 7v10h16V7l-8 6z"/></symbol>
  <symbol id="icon-globe" viewBox="0 0 24 24"><path d="M12 2a10 10 0 1 0 0 20 10 10 0 0 0 0-20zm7.9 9h-3.5a15 15 0 0 0-1.3-6A8 8 0 0 1 19.9 11zM12 4c.9 1.3 1.9 3.8 2.1 7H9.9C10.1 7.8 11.1 5.3 12 4zM8.9 5a15 15 0 0 0-1.3 6H4.1A8 8 0 0 1 8.9 5zM4.1 13h3.5a15 15 0 0 0 1.3 6A8 8 0 0 1 4.1 13zM12 20c-.9-1.3-1.9-3.8-2.1-7h4.2c-.2 3.2-1.2 5.7-2.1 7zm3.1-1a15 15 0 0 0 1.3-6h3.5a8 8 0 0 1-4.8 6z"/></symbol>
</svg>

<main class="canvas">

  <section class="sheet letterhead" aria-label="Letterhead">
    <div class="wordmark">Ridgeline Elite</div>
    <div class="divider"></div>
    <ul class="contact">
      <li><svg><use href="#icon-phone"/></svg>555-014-2870</li>
      <li><svg><use href="#icon-mail"/></svg>hello@ridgelineelite.com</li>
      <li><svg><use href="#icon-globe"/></svg>www.ridgelineelite.com</li>
    </ul>
    <div class="letter-body">
      <p class="date">01 January 2050</p>
      <p class="recipient"><strong>Company (Pvt) Ltd.</strong><br>PO Box 3355 Mainville St<br>Sample City Country 3355</p>
      <p class="salutation">Dear Mara Linwood,</p>
      <p class="para">Lorem ipsum dolor sit amet, consectetuer adipiscing elit, sed diam nonummy nibh euismod tincidunt ut laoreet dolore magna aliquam erat volutpat. Ut wisi enim ad minim veniam, quis nostrud exerci tation ullamcorper suscipit lobortis nisl ut aliquip ex ea commodo consequat. Duis dolore te feugait nulla facilisi. Nam liber tempor cum soluta nobis eleifend option congue nihil imperdiet doming id quod mazim placerat facer possim assum. Lorem ipsum dolor sit amet, consectetuer adipiscing elit, sed diam nonummy nibh euismod tincidunt ut laoreet dolore magna aliquam erat volutpat. Ut wisi enim ad minim veniam, quis nostrud exerci tation ullamcorper suscipit lobortis nisl ut aliquip ex ea commodo consequat.</p>
      <p class="para">Consectetuer adipiscing elit, sed diam nonummy nibh euismod tincidunt ut laoreet dolore magna aliquam erat volutpat. Ut wisi enim ad minim veniam, quis nostrud exerci tation ullamcorper suscipit lobortis nisl ut aliquip ex ea commodo consequat. Consectetuer adipiscing elit, sed diam nonummy nibh euismod tincidunt ut laoreet dolore magna aliquam erat volutpat. Ut wisi enim ad minim veniam, quis nostrud exerci tation ullamcorper suscipit lobortis nisl ut aliquip ex ea commodo consequat.</p>
      <p class="para">Consectetuer adipiscing elit, sed diam nonummy nibh euismod tincidunt ut laoreet dolore magna aliquam erat volutpat. Ut wisi enim ad minim veniam, quis nostrud exerci tation ullamcorper suscipit lobortis nisl ut aliquip ex ea commodo consequat. Consectetuer adipiscing elit, sed diam nonummy nibh euismod tincidunt ut laoreet dolore magna aliquam erat volutpat. Ut wisi enim ad minim veniam, quis nostrud exerci tation ullamcorper suscipit lobortis nisl ut aliquip ex ea commodo consequat.</p>
      <p class="closing">Sincerely Yours</p>
      <p class="signature">Thomas Reed Calloway</p>
    </div>
    <div class="band"><div class="band-navy">Ridgeline Elite, Maple Hollow 40100, USA</div></div>
  </section>

  <section class="sheet envelope" aria-label="Envelope">
    <div class="wordmark">Ridgeline Elite</div>
    <div class="dash"></div>
    <ul class="contact">
      <li><svg><use href="#icon-phone"/></svg>555-014-2870</li>
      <li><svg><use href="#icon-mail"/></svg>hello@ridgelineelite.com</li>
      <li><svg><use href="#icon-globe"/></svg>www.ridgelineelite.com</li>
    </ul>
    <div class="band"><div class="band-navy">Ridgeline Elite, Maple Hollow 40100, USA</div></div>
  </section>

  <section class="sheet card card-front card-front-a" aria-label="Business card front">
    <div class="wordmark">Ridgeline Elite</div>
    <div class="divider"></div>
    <div class="details">
      <p class="name">Evan Hollister</p>
      <p class="role">Founder &amp; CEO</p>
      <p class="address">Ridgeline Elite<br>Maple Hollow 40100, USA</p>
      <ul class="contact">
        <li><svg><use href="#icon-phone"/></svg>555-014-2870</li>
        <li><svg><use href="#icon-mail"/></svg>hello@ridgelineelite.com</li>
        <li><svg><use href="#icon-globe"/></svg>www.ridgelineelite.com</li>
      </ul>
    </div>
    <div class="band"><div class="band-navy"></div></div>
  </section>

  <section class="sheet card card-back" aria-label="Business card back">
    <div class="wordmark">Ridgeline Elite</div>
  </section>

  <section class="sheet card card-front card-front-b" aria-label="Business card front">
    <div class="wordmark">Ridgeline Elite</div>
    <div class="divider"></div>
    <div class="details">
      <p class="name">Evan Hollister</p>
      <p class="role">Founder &amp; CEO</p>
      <p class="address">Ridgeline Elite<br>Maple Hollow 40100, USA</p>
      <ul class="contact">
        <li><svg><use href="#icon-phone"/></svg>555-014-2870</li>
        <li><svg><use href="#icon-mail"/></svg>hello@ridgelineelite.com</li>
        <li><svg><use href="#icon-globe"/></svg>www.ridgelineelite.com</li>
      </ul>
    </div>
    <div class="band"><div class="band-navy"></div></div>
  </section>

</main>
</body>
</html>
```